Business Card Design for Fashion Tech Startup

Dear designers, we need a business card for Asia's premier fashion tech startup.!

PebbleHop is discovery e-commerce destination for busy, discerning parents in Asia featuring leading independent designers of baby, kids fashion apparel and sustainable brands from around the world.

PebbleHop is a modern, contemporary fashion tech startup targeting well-educated, well travelled and affluent parents. We're NOT your typical kiddy store!! Our design philosophy & e-commerce site is more like Vask.com, Orimesa.com, Pondwick.com, Farthollow.com.
Updates

Hi, size of the business card should be 84mm X 55mm. Would appreciate some business card layouts in Portrait as added consideration, i fancy the idea of a Portrait business card. What's important is that the business card should pique the receiver's interest to log onto the website to learn more. Many thanks and love forward to the designs!

Target Market(s)

Though modern, classy in look, feel & positioning, PebbleHop does possess a cheeky, fun-loving personality as depicted by its logo and the segment it targets (baby, kids) though the key decision makers i.e primarily mums between 25-40 who are well educated/travelled, local & expatriates, internet/digitally savvy, mid-high income working mums.

Industry/Entity Type

E-Commerce

Requirements
Must have
• Name, designation, email, phone & mobile number.
Company url : www.pebblehop.sg
Slogan : Discovery e-commerce destination for discerning, busy parents
Nice to have
• Call to Action such as a Discount code offering 10% discount
or asking people to "Like" us on our Chatterly page/Chatterly URL

```html
<!DOCTYPE html>
<html lang="en">
<head>
<meta charset="utf-8">
<title>PebbleHop Business Card</title>
<link rel="stylesheet" href="https://fonts.googleapis.com/css2?family=Sniglet:wght@800&family=Gochi+Hand&family=Amatic+SC:wght@700&family=Arimo&display=swap">
<style>
  :root {
    --backdrop: #3b3b3b;
    --card: #ffffff;
    --navy: #35566b;
    --coral: #f57f6c;
    --ink: #2f4e63;
  }
  * { margin: 0; padding: 0; box-sizing: border-box; }
  html, body { width: 1200px; height: 1000px; overflow: hidden; background: var(--backdrop); }
  .canvas { position: relative; width: 1200px; height: 1000px; }

  .card {
    position: absolute;
    background: var(--card);
    border-radius: 24px;
    width: 460px;
    height: 702px;
    top: 140px;
  }
  .card--front { left: 80px; }
  .card--back { left: 670px; }

  /* Front */
  .brand-mark {
    position: absolute;
    left: 162px; top: 40px;
    width: 136px; height: 136px;
    border-radius: 50%;
    background: var(--navy);
  }
  .brand-name {
    position: absolute;
    left: 0; right: 0; top: 206px;
    text-align: center;
    font-family: "Sniglet", "Arial Rounded MT Bold", sans-serif;
    font-weight: 800;
    font-size: 60px;
    line-height: 76px;
    color: var(--navy);
    letter-spacing: 1px;
  }
  .divider {
    position: absolute;
    left: 50px; top: 302px;
    width: 376px; height: 2px;
    background: linear-gradient(to right, var(--coral) 0 50%, var(--navy) 50% 100%);
    opacity: .8;
  }
  .site-url {
    position: absolute;
    left: 0; right: 0; top: 310px;
    text-align: center;
    font-family: "Arimo", Arial, sans-serif;
    font-size: 25px;
    line-height: 30px;
    letter-spacing: 2.5px;
    color: var(--ink);
  }
  .slogan {
    position: absolute;
    left: 0; right: 0; top: 356px;
    text-align: center;
    font-family: "Gochi Hand", cursive;
    font-size: 18px;
    line-height: 21px;
    letter-spacing: 1.6px;
    color: var(--ink);
  }
  .person-name {
    position: absolute;
    left: 0; right: 0; top: 448px;
    text-align: center;
    font-family: "Amatic SC", cursive;
    font-weight: 700;
    font-size: 52px;
    line-height: 56px;
    letter-spacing: 2px;
    color: var(--ink);
  }
  .person-role {
    position: absolute;
    left: 0; right: 0; top: 506px;
    text-align: center;
    font-family: "Arimo", Arial, sans-serif;
    font-size: 20px;
    line-height: 24px;
    letter-spacing: 1px;
    color: var(--ink);
  }
  .contact {
    position: absolute;
    left: 0; right: 0; top: 564px;
    text-align: center;
    font-family: "Arimo", Arial, sans-serif;
    font-size: 20px;
    line-height: 35px;
    color: var(--ink);
    list-style: none;
  }

  /* Back */
  .pattern-field {
    position: absolute;
    left: 0; top: 125px;
    width: 460px; height: 460px;
    border-radius: 50%;
    background: radial-gradient(circle at 50% 42%, #ffffff 0 22%, rgba(245,127,108,.55) 23%, rgba(53,86,107,.45) 100%);
  }
  .back-mark {
    position: absolute;
    left: 160px; top: 245px;
    width: 150px; height: 150px;
    border-radius: 50%;
    background: var(--navy);
  }
  .back-name {
    position: absolute;
    left: 0; right: 0; top: 440px;
    text-align: center;
    font-family: "Sniglet", "Arial Rounded MT Bold", sans-serif;
    font-weight: 800;
    font-size: 44px;
    line-height: 56px;
    color: var(--navy);
  }
</style>
</head>
<body>
<main class="canvas">
  <section class="card card--front">
    <div class="brand-mark"></div>
    <h1 class="brand-name">PebbleHop</h1>
    <div class="divider"></div>
    <p class="site-url">www.PebbleHop.sg</p>
    <p class="slogan">discovery e-commerce destination<br>for discerning, busy parents</p>
    <h2 class="person-name">Mara Quill</h2>
    <p class="person-role">Marketing Head</p>
    <ul class="contact">
      <li>maraquill@pebblehop.sg</li>
      <li>+65 - 555 010 2030</li>
      <li>55501234</li>
    </ul>
  </section>

  <section class="card card--back">
    <div class="pattern-field" role="img" aria-label="Round cluster of small baby and kids items: clothes, toys, bottles, shoes, stars and hearts in coral and navy"></div>
    <div class="back-mark"></div>
    <p class="back-name">PebbleHop.sg</p>
  </section>
</main>
</body>
</html>
```